Bakery Business Cards

We are in need of business cards for our bakery business--something non-generic that reflects our business and will stand out. We are a wholesale bakery that primarily services in-store bakeries, casinos, schools, distributors, and fund-raising companies. The family business was founded in 1960. (www.marlowsovenworks.com)

```html
<!DOCTYPE html>
<html lang="en">
<head>
<meta charset="utf-8">
<title>Marlow's Ovenworks – Business Cards</title>
<link href="https://fonts.googleapis.com/css2?family=Lato:wght@400;700;900&display=swap" rel="stylesheet">
<style>
  :root {
    --backdrop: #cdcdcd;
    --card-white: #ffffff;
    --brand-blue: #2f4ea3;
    --brand-blue-soft: #4463b3;
    --ink: #3a3a3a;
    --pastry: #e8cfa4;
    --berry: #a8434a;
    --plate: #f3efe8;
  }
  * { margin: 0; padding: 0; box-sizing: border-box; }
  html, body {
    width: 1200px; height: 800px; overflow: hidden;
    background: var(--backdrop);
    font-family: "Lato", Arial, sans-serif;
  }
  .canvas { position: relative; width: 1200px; height: 800px; }

  .card {
    position: absolute; left: 390px; width: 420px; height: 240px;
    border-radius: 12px; overflow: hidden;
  }
  .card-front { top: 130px; background: var(--card-white); }
  .card-back { top: 430px; }

  .front-photo {
    position: absolute; top: 0; right: 0; width: 62%; height: 100%;
    background:
      radial-gradient(circle at 60% 55%, rgba(168,67,74,.55) 0 12%, transparent 20%),
      radial-gradient(circle at 40% 20%, rgba(232,207,164,.9) 0 14%, transparent 24%),
      radial-gradient(circle at 90% 40%, rgba(168,67,74,.4) 0 8%, transparent 16%),
      radial-gradient(circle at 45% 85%, rgba(232,207,164,.8) 0 12%, transparent 22%),
      linear-gradient(90deg, var(--plate), #d9b98a);
    -webkit-mask-image: linear-gradient(90deg, transparent 0%, rgba(0,0,0,.35) 25%, #000 60%);
            mask-image: linear-gradient(90deg, transparent 0%, rgba(0,0,0,.35) 25%, #000 60%);
  }
  .name-tab {
    position: absolute; left: -22px; top: 34px;
    width: 44px; height: 44px; border-radius: 50%;
    background: var(--brand-blue);
  }
  .person { position: absolute; left: 28px; top: 38px; }
  .person-name {
    font-weight: 900; font-size: 22px; letter-spacing: -.2px;
    color: var(--brand-blue); line-height: 1;
  }
  .person-title { font-size: 13px; color: var(--ink); margin-top: 4px; }

  .contact {
    position: absolute; left: 28px; top: 144px;
    font-size: 12px; color: var(--ink); line-height: 14px;
  }
  .contact-address { margin-bottom: 3px; }
  .contact-row { display: flex; align-items: center; gap: 9px; height: 15px; }
  .contact-row svg { width: 11px; height: 11px; flex: none; }

  .back-photo {
    position: absolute; inset: 0;
    background:
      radial-gradient(circle at 25% 20%, rgba(255,255,255,.08) 0 18%, transparent 26%),
      radial-gradient(circle at 75% 35%, rgba(255,255,255,.08) 0 20%, transparent 28%),
      radial-gradient(circle at 12% 60%, rgba(0,0,0,.06) 0 14%, transparent 20%),
      radial-gradient(circle at 90% 80%, rgba(255,255,255,.06) 0 14%, transparent 20%),
      var(--brand-blue-soft);
  }
  .brand {
    position: absolute; inset: 0;
    display: flex; align-items: center; justify-content: center;
    color: var(--card-white); font-weight: 900;
  }
  .brand-name { font-size: 34px; letter-spacing: .2px; }
</style>
</head>
<body>
<main class="canvas">

  <section class="card card-front">
    <div class="front-photo" role="img" aria-label="Overhead photo of fruit pies and berry cobblers on white plates"></div>
    <div class="name-tab"></div>
    <div class="person">
      <div class="person-name">DANIEL MARLOW</div>
      <div class="person-title">Founder &amp; CEO</div>
    </div>
    <div class="contact">
      <div class="contact-address">1170 Hearth Lane,<br>Oklahoma City, OK 73109</div>
      <div class="contact-row">
        <svg viewBox="0 0 24 24" fill="var(--brand-blue)"><path d="M6.6 10.8a15 15 0 0 0 6.6 6.6l2.2-2.2a1 1 0 0 1 1-.25 11.4 11.4 0 0 0 3.6.57 1 1 0 0 1 1 1V20a1 1 0 0 1-1 1A17 17 0 0 1 3 4a1 1 0 0 1 1-1h3.5a1 1 0 0 1 1 1c0 1.25.2 2.45.57 3.6a1 1 0 0 1-.25 1z"/></svg>
        <span>(405) 555-0148</span>
      </div>
      <div class="contact-row">
        <svg viewBox="0 0 24 24"><rect x="2" y="5" width="20" height="14" fill="var(--brand-blue)"/><path d="M2 5l10 8 10-8" stroke="#fff" stroke-width="1.6" fill="none"/></svg>
        <span>sales@marlowsovenworks.com</span>
      </div>
      <div class="contact-row">
        <svg viewBox="0 0 24 24" fill="none" stroke="var(--brand-blue)" stroke-width="1.8"><circle cx="12" cy="12" r="9.5"/><path d="M2.5 12h19M12 2.5c3 3 3 16 0 19M12 2.5c-3 3-3 16 0 19"/></svg>
        <span>www.marlowsovenworks.com</span>
      </div>
    </div>
  </section>

  <section class="card card-back">
    <div class="back-photo" role="img" aria-label="Blue-tinted overhead photo of pies and cobblers"></div>
    <div class="brand">
      <div class="brand-name">Marlow's Ovenworks</div>
    </div>
  </section>

</main>
</body>
</html>
```